Expanding Training Company needs a powerpoint template to deliver a consistent professional image

We want to start with a ppt template that is clean and flexible.
We are a small training organisation focusing on personal effectiveness, leadership, management and change. The MD is a New Zealander living in the United Kingdom and loves the idea of the clean green image that NZ has and wants the PowerPoint template to reflect that. We are pragmatic in what we do - everything comes back to performance improvement. Our clients are big players and our presentations need to be as clean, and as professional as theirs. We need a template that is versatile and can have their logos added as necessary.
Our training tends to be very current and as such we would like to use a lot of images and less words/bullets. We have company colours, logos and fonts that we are happy with and will continue to use.

Here are our company values to give you a sense of what we are about…

As a learning organisation we are always looking to continually improve and renew, our material, ideas, and methods, and are continually on the look out for new techniques, interventions and applications that provide measurable results to our clients.

We think life is about people and relationships, and we are prepared to walk away if people don't keep their word, are untrustworthy or lack integrity, as life is just too short to work with arses.
And because we are not arses we admit when we are wrong and make good on our commitments.

For our clients its all about performance and training is a performance enhancer, we aim to provide training excellence tin all its guises that delivers performance and happy clients.

We harness the value of the team, we believe in Interdependence.

We make life easier for our clients and each other.

Flexibility, innovation and future focus/vision are what our clients can count on us for.

Work is one of many of life's great facilitators, we recognise and value the others - its not just about work.

Industry/Entity Type

It Company

Other font styles liked:
• Avenir Next

Colors
abd037
9bcb3c

Requirements
Must have
• A clean look with multiple options for inserting images, tables, videos, text boxes etc
• copyright information
Nice to have
• Slide masters

```html
<!DOCTYPE html>
<html lang="en">
<head>
<meta charset="utf-8">
<title>Kauri Learning – Presentation Template Overview</title>
<link rel="stylesheet" href="https://fonts.googleapis.com/css2?family=Nunito+Sans:wght@300;400;600&display=swap">
<style>
:root{
  --green-deep:#1a9c3e;
  --green:#3aad45;
  --green-light:#9bcb3c;
  --green-lime:#abd037;
  --ink:#5d6660;
  --muted:#9aa19c;
  --rule:#3aad45;
  --paper:#ffffff;
  --page:#ffffff;
  --shadow:rgba(0,0,0,.16);
}
*{box-sizing:border-box;margin:0;padding:0}
html,body{width:672px;height:1200px;overflow:hidden;background:var(--page)}
body{font-family:"Nunito Sans",Arial,sans-serif;color:var(--ink)}
.deck{
  width:672px;height:1200px;padding:5px 3px;
  display:grid;grid-template-columns:repeat(3,218px);grid-auto-rows:122px;
  column-gap:6px;row-gap:11px;
}
.slide{position:relative;overflow:hidden;background:var(--paper);box-shadow:0 1px 3px var(--shadow)}
.slide.closing{grid-column:2}
.abs{position:absolute}
.green{background:linear-gradient(90deg,var(--green-deep),var(--green-light))}
.green-v{background:linear-gradient(180deg,var(--green-light),var(--green-deep))}
.green-cover{background:linear-gradient(180deg,#5fb94a 0%,#3aad45 45%,#1f9f3e 100%)}
.white-text{color:#fff}

/* photo placeholders */
.photo{position:absolute}
.ph-lake{background:linear-gradient(180deg,#8fb3d6 0%,#3f7fae 45%,#2e6a93 65%,#5b7244 100%)}
.ph-hills{background:linear-gradient(180deg,#5e8ccc 0%,#a9c2de 35%,#e2c35e 55%,#8b7a33 100%)}
.ph-snow{background:linear-gradient(180deg,#5e92c9 0%,#dfe8ef 45%,#8a9690 70%,#4f6048 100%)}
.ph-forest{background:linear-gradient(180deg,#30462c 0%,#5d7f45 55%,#2b3b27 100%)}
.ph-falls{background:linear-gradient(90deg,#2f442a 0%,#5d7b44 40%,#dfe6e4 50%,#5d7b44 60%,#2f442a 100%)}
.ph-sunset{background:linear-gradient(180deg,#ecc46a 0%,#b28aa6 40%,#6b6a8e 55%,#4a5e3c 100%)}
.ph-dusk{background:linear-gradient(180deg,#f0d98a 0%,#9aa7a8 45%,#4d5b55 100%)}
.ph-storm{background:linear-gradient(180deg,#414c57 0%,#8794a0 45%,#a9b6bd 60%,#3b5466 100%)}
.ph-valley{background:linear-gradient(180deg,#7fa6d2 0%,#cfd8dc 40%,#8a8a5c 60%,#5c6a3a 100%)}
.ph-coast{background:linear-gradient(180deg,#7eb3dc 0%,#3d8fb8 50%,#e6dcc0 75%,#6d8d52 100%)}
.ph-frost{background:radial-gradient(circle at 40% 40%,#f2f4f1 0%,#b9c0b8 45%,#4a524b 100%)}
.ph-person{background:linear-gradient(180deg,#eceeee 0%,#c9cccc 40%,#2c303a 60%,#23262e 100%)}

/* brand */
.brand{display:flex;align-items:center;gap:2px;font-weight:400;color:var(--green);font-size:5px;line-height:1}
.brand .mark{width:4px;height:4px;background:var(--green);border-radius:50%}
.brand.on-green{color:#fff}
.brand.on-green .mark{background:#fff}
.brand.large{font-size:8px;gap:4px}
.brand.large .mark{width:7px;height:7px}

/* slide furniture */
.footer{position:absolute;left:0;right:0;bottom:0;height:12px}
.footer .brand{position:absolute;left:5px;bottom:4px}
.footer .rule{position:absolute;left:42px;right:6px;bottom:5px;height:.6px;background:var(--rule)}
.footer .legal{position:absolute;right:14px;bottom:6.5px;font-size:2px;color:var(--muted)}
.footer .page{position:absolute;right:6px;bottom:6.5px;font-size:2px;color:var(--muted)}
.slide-title{position:absolute;left:10px;top:8px;font-size:8px;font-weight:400;color:var(--green);letter-spacing:.1px;text-transform:uppercase}
.body{font-size:2.6px;line-height:1.45;color:var(--muted)}
.body-white{font-size:2.6px;line-height:1.45;color:#fff}
.statement{font-weight:400;line-height:1.2;color:var(--green)}
.statement.on-green{color:#fff}
.center{text-align:center}
.right{text-align:right}

/* cover */
.cover-title{position:absolute;right:12px;color:#fff;text-align:right}
.cover-title h1{font-size:9.5px;font-weight:300}
.cover-title p{font-size:4px;font-weight:300;margin-top:1px}
.cover-line{position:absolute;height:.6px;background:rgba(255,255,255,.8)}

/* agenda */
.agenda-item{position:absolute;display:flex;gap:4px;width:80px}
.agenda-item .time{width:16px;height:5.5px;background:var(--green);color:#fff;font-size:2.4px;display:flex;align-items:center;justify-content:center;flex:none;margin-top:1px}
.agenda-item h3{font-size:3.6px;font-weight:400;color:var(--green)}
.agenda-item p{font-size:2.2px;color:var(--muted);line-height:1.4}

/* presenters */
.presenter{position:absolute;bottom:10px;display:flex;align-items:center;gap:2px;font-size:3px;color:var(--ink)}
.presenter .label{font-size:2.2px;color:var(--muted)}
.badge{position:absolute;right:10px;bottom:8px;width:30px;height:12px;background:#d9dcda}

/* icon circles */
.icon-dot{position:absolute;width:18px;height:18px;border-radius:50%;background:var(--green);display:flex;align-items:center;justify-content:center}
.skill{font-size:2.4px;color:var(--ink);margin-top:3px}
.bar{height:1.4px;background:#e3e6e4;width:34px;position:relative;margin-top:1px}
.bar span{position:absolute;left:0;top:0;bottom:0;background:var(--green)}
</style>
</head>
<body>
<main class="deck">

  <!-- 1 cover -->
  <section class="slide green-cover">
    <div class="photo" style="inset:0;background:linear-gradient(180deg,rgba(255,255,255,.08),rgba(0,0,0,.06))" role="img" aria-label="Green-toned mountain valley landscape"></div>
    <div class="brand large on-green abs" style="left:52px;top:56px">Kauri Learning</div>
    <div class="cover-line" style="left:100px;right:12px;top:73px"></div>
    <div class="cover-title" style="top:53px"><h1>Your Title Goes Here</h1><p>Your Subtitle Goes Here</p></div>
  </section>

  <!-- 2 cover with presenters -->
  <section class="slide">
    <div class="photo green-cover" style="left:0;top:0;right:0;height:93px" role="img" aria-label="Green-toned mountain lake landscape"></div>
    <div class="brand large on-green abs" style="left:22px;top:48px">Kauri Learning</div>
    <div class="cover-title" style="top:43px"><h1>Your Title Goes Here</h1><p>Your Subtitle Goes Here</p></div>
    <div class="presenter" style="left:12px"><span class="label">Presented by</span></div>
    <div class="presenter" style="left:30px"><svg width="5" height="5" viewBox="0 0 10 10"><circle cx="5" cy="3" r="2.4" fill="#3aad45"/><path d="M1 10a4 4 0 0 1 8 0z" fill="#3aad45"/></svg><div>Alex Reid<br><span class="label">Lead Trainer</span></div></div>
    <div class="presenter" style="left:66px"><svg width="5" height="5" viewBox="0 0 10 10"><circle cx="5" cy="3" r="2.4" fill="#3aad45"/><path d="M1 10a4 4 0 0 1 8 0z" fill="#3aad45"/></svg><div>Sam Carter<br><span class="label">Facilitator</span></div></div>
    <div class="presenter" style="left:148px"><span class="label">Partner</span></div>
    <div class="badge"></div>
  </section>

  <!-- 3 agenda -->
  <section class="slide">
    <h2 class="slide-title">Our Agenda</h2>
    <div class="agenda-item" style="left:12px;top:30px"><div class="time">10:00</div><div><h3>Agenda One</h3><p>Short note about this session topic.</p></div></div>
    <div class="agenda-item" style="left:12px;top:55px"><div class="time">11:00</div><div><h3>Agenda Two</h3><p>Short note about this session topic.</p></div></div>
    <div class="agenda-item" style="left:12px;top:80px"><div class="time">12:00</div><div><h3>Agenda Three</h3><p>Short note about this session topic.</p></div></div>
    <div class="agenda-item" style="left:112px;top:30px"><div class="time">13:00</div><div><h3>Agenda Four</h3><p>Short note about this session topic.</p></div></div>
    <div class="agenda-item" style="left:112px;top:55px"><div class="time">14:00</div><div><h3>Agenda Five</h3><p>Short note about this session topic.</p></div></div>
    <div class="agenda-item" style="left:112px;top:80px"><div class="time">15:00</div><div><h3>Agenda Six</h3><p>Short note about this session topic.</p></div></div>
  </section>

  <!-- 4 quote -->
  <section class="slide">
    <h2 class="slide-title">Quote Area</h2>
    <div class="green abs" style="left:0;top:26px;width:112px;height:76px;padding:14px 10px 0 14px">
      <p style="font-size:4.2px;color:#fff;line-height:1.3">“ Coming together is a beginning. Keeping together is progress. Working together is success. ”</p>
      <p style="font-size:4.2px;color:#fff;margin-top:6px">- Marcus Hale -</p>
    </div>
    <div class="photo ph-dusk" style="left:112px;top:26px;right:0;height:76px" role="img" aria-label="Golden grassland below mountains at sunrise"></div>
    <div class="footer"><div class="brand">Kauri Learning</div><div class="rule"></div><div class="legal">© 2024 Kauri Learning. All rights reserved</div><div class="page">2</div></div>
  </section>

  <!-- 5 mosaic -->
  <section class="slide">
    <div class="green abs" style="left:0;top:0;width:109px;height:38px;padding:3px 5px"><p class="body-white">Lorem ipsum dolor sit amet, consectetur adipiscing elit, sed do eiusmod tempor incididunt ut labore et dolore magna aliqua ut enim ad minim veniam.</p></div>
    <div class="photo ph-snow" style="left:109px;top:0;right:0;height:38px" role="img" aria-label="Snow-capped mountain range under blue sky"></div>
    <div class="photo ph-snow" style="left:0;top:38px;width:109px;height:46px" role="img" aria-label="Snowy peaks above a green valley"></div>
    <div class="green abs" style="left:109px;top:38px;right:0;height:46px;padding:8px 5px"><p class="body-white">Lorem ipsum dolor sit amet, consectetur adipiscing elit, sed do eiusmod tempor incididunt ut labore et dolore magna aliqua ut enim ad minim veniam.</p></div>
    <div class="green abs" style="left:0;top:84px;width:109px;bottom:0;padding:4px 5px"><p class="body-white">Lorem ipsum dolor sit amet, consectetur adipiscing elit, sed do eiusmod tempor incididunt ut labore et dolore magna aliqua.</p></div>
    <div class="photo ph-snow" style="left:109px;top:84px;right:0;bottom:0" role="img" aria-label="Glacier mountain ridge"></div>
  </section>

  <!-- 6 title + grid -->
  <section class="slide">
    <h2 class="slide-title">Your Title Goes Here</h2>
    <div class="photo ph-valley" style="left:15px;top:26px;width:60px;height:36px" role="img" aria-label="Country road through mountains"></div>
    <div class="green abs" style="left:78px;top:26px;width:60px;height:36px;padding:3px"><p style="font-size:4px;color:#fff">Heading Goes Here</p><p class="body-white" style="font-size:2px">Lorem ipsum dolor sit amet consectetur adipiscing elit sed do.</p></div>
    <div class="photo ph-coast" style="left:141px;top:26px;width:60px;height:36px" role="img" aria-label="Turquoise hot spring pool"></div>
    <div class="green abs" style="left:15px;top:64px;width:60px;height:36px;padding:3px"><p style="font-size:4px;color:#fff">Heading Goes Here</p><p class="body-white" style="font-size:2px">Lorem ipsum dolor sit amet consectetur adipiscing elit sed do.</p></div>
    <div class="photo ph-lake" style="left:78px;top:64px;width:60px;height:36px" role="img" aria-label="Blue lake between forested hills"></div>
    <div class="green abs" style="left:141px;top:64px;width:60px;height:36px;padding:3px"><p style="font-size:4px;color:#fff">Heading Goes Here</p><p class="body-white" style="font-size:2px">Lorem ipsum dolor sit amet consectetur adipiscing elit sed do.</p></div>
    <div class="footer"><div class="brand">Kauri Learning</div><div class="rule"></div><div class="legal">© 2024 Kauri Learning. All rights reserved</div><div class="page">4</div></div>
  </section>

  <!-- 7 about us -->
  <section class="slide">
    <div class="photo ph-lake" style="left:0;top:18px;width:152px;height:86px" role="img" aria-label="Rocky mountain beside a calm lake"></div>
    <div class="green abs" style="left:110px;top:26px;right:0;height:66px;padding:10px 8px">
      <h2 style="font-size:7px;font-weight:400;color:#fff">ABOUT US</h2>
      <p class="body-white" style="margin-top:4px">Lorem ipsum dolor sit amet, consectetur adipiscing elit, sed do eiusmod tempor incididunt ut labore et dolore magna aliqua.</p>
      <p class="body-white" style="margin-top:3px">Ut enim ad minim veniam, quis nostrud exercitation ullamco laboris nisi ut aliquip ex ea commodo.</p>
    </div>
    <div class="footer"><div class="brand">Kauri Learning</div><div class="rule"></div><div class="legal">© 2024 Kauri Learning. All rights reserved</div><div class="page">5</div></div>
  </section>

  <!-- 8 two pictures -->
  <section class="slide">
    <h2 class="slide-title">Two Pictures Slide</h2>
    <div class="photo ph-falls" style="left:16px;top:22px;width:92px;height:84px" role="img" aria-label="Waterfall in dense forest"></div>
    <div class="photo ph-falls" style="left:112px;top:22px;width:92px;height:84px" role="img" aria-label="Tall waterfall over a mossy cliff"></div>
    <div class="footer"><div class="brand">Kauri Learning</div><div class="rule"></div><div class="legal">© 2024 Kauri Learning. All rights reserved</div><div class="page">6</div></div>
  </section>

  <!-- 9 title and image + text -->
  <section class="slide">
    <h2 class="slide-title">Title and Image + Text</h2>
    <div class="photo ph-sunset" style="left:15px;top:24px;width:188px;height:46px" role="img" aria-label="Volcano at dusk above a highway"></div>
    <p class="abs" style="left:15px;top:74px;width:82px;font-size:3.8px;line-height:1.3;color:var(--green)">Lorem ipsum dolor sit amet, consectetur adipiscing elit, sed do eiusmod tempor incididunt ut labore et dolore magna aliqua. Ut enim ad minim veniam, quis</p>
    <p class="abs body" style="left:112px;top:74px;width:90px">Lorem ipsum dolor sit amet, consectetur adipiscing elit, sed do eiusmod tempor incididunt ut labore et dolore magna aliqua. Ut enim ad minim veniam, quis nostrud exercitation ullamco laboris nisi ut aliquip ex ea commodo consequat.</p>
    <div class="footer"><div class="brand">Kauri Learning</div><div class="rule"></div><div class="legal">© 2024 Kauri Learning. All rights reserved</div><div class="page">7</div></div>
  </section>

  <!-- 10 three bullets -->
  <section class="slide">
    <h2 class="slide-title">Three Bullets Area</h2>
    <div class="photo ph-hills" style="left:0;top:20px;right:0;height:52px" role="img" aria-label="Golden farmland plains beneath mountains"></div>
    <div class="icon-dot" style="left:36px;top:63px"><svg width="9" height="9" viewBox="0 0 10 10" fill="none" stroke="#fff" stroke-width=".9"><circle cx="2.5" cy="5" r="1.3"/><circle cx="7.5" cy="2.3" r="1.3"/><circle cx="7.5" cy="7.7" r="1.3"/><path d="M3.6 4.4 6.4 2.9M3.6 5.6 6.4 7.1"/></svg></div>
    <div class="icon-dot" style="left:100px;top:63px"><svg width="9" height="9" viewBox="0 0 10 10" fill="none" stroke="#fff" stroke-width=".9"><path d="M5 1 9 3 5 5 1 3Z"/><path d="M1 5 5 7 9 5M1 7 5 9 9 7"/></svg></div>
    <div class="icon-dot" style="left:164px;top:63px"><svg width="9" height="9" viewBox="0 0 10 10" fill="none" stroke="#fff" stroke-width=".9"><path d="M2 9h6M3 9l1-3h2l1 3M4 6 3.5 3 5 1.5 6.5 3 6 6"/></svg></div>
    <p class="abs body center" style="left:22px;top:85px;width:46px;font-size:2.2px">Lorem ipsum dolor sit amet, consectetur adipiscing elit sed do eiusmod.</p>
    <p class="abs body center" style="left:86px;top:85px;width:46px;font-size:2.2px">Lorem ipsum dolor sit amet, consectetur adipiscing elit sed do eiusmod.</p>
    <p class="abs body center" style="left:150px;top:85px;width:46px;font-size:2.2px">Lorem ipsum dolor sit amet, consectetur adipiscing elit sed do eiusmod.</p>
    <div class="footer"><div class="brand">Kauri Learning</div><div class="rule"></div><div class="legal">© 2024 Kauri Learning. All rights reserved</div><div class="page">10</div></div>
  </section>

  <!-- 11 people statement -->
  <section class="slide">
    <div class="photo ph-lake" style="left:0;top:0;width:72px;bottom:0" role="img" aria-label="Mountain lake beside a lakeside town"></div>
    <div class="photo ph-lake" style="left:74px;top:0;width:72px;bottom:0" role="img" aria-label="Deep blue lake framed by steep hills"></div>
    <div class="green-v abs" style="left:148px;top:0;right:0;bottom:0;padding:40px 6px 0 6px">
      <p class="statement on-green" style="font-size:7.5px">We Think Life Is About People And Relationships</p>
    </div>
  </section>

  <!-- 12 team statement -->
  <section class="slide">
    <p class="abs statement" style="left:10px;top:30px;width:100px;font-size:7.2px">We Harness The Value Of The Team, We Believe In Interdependence.</p>
    <div class="photo ph-storm" style="left:110px;top:0;right:0;bottom:0" role="img" aria-label="Wooden jetty on a lake under storm clouds"></div>
  </section>

  <!-- 13 flexibility with three photos -->
  <section class="slide">
    <p class="abs statement center" style="left:20px;right:20px;top:14px;font-size:7.5px">Flexibility, Innovation And Future Focus/Vision Are What Our Clients Can Count On Us For.</p>
    <div class="photo ph-valley" style="left:0;top:72px;width:71px;bottom:0" role="img" aria-label="Lone tree on a hillside"></div>
    <div class="photo ph-sunset" style="left:73px;top:72px;width:72px;bottom:0" role="img" aria-label="Mountains at sunset"></div>
    <div class="photo ph-coast" style="left:147px;top:72px;right:0;bottom:0" role="img" aria-label="Curved beach bay"></div>
  </section>

  <!-- 14 collage -->
  <section class="slide">
    <div class="photo ph-valley" style="left:0;top:0;width:54px;height:40px" role="img" aria-label="Rocky alpine outcrop"></div>
    <div class="green abs" style="left:56px;top:0;width:54px;height:40px;padding:7px 4px"><p class="statement on-green" style="font-size:4.2px">We Think Life Is About People And Relationships</p></div>
    <div class="photo ph-snow" style="left:112px;top:0;right:0;height:78px" role="img" aria-label="Rugged mountain above forest"></div>
    <div class="photo ph-hills" style="left:0;top:42px;width:110px;bottom:0" role="img" aria-label="Tussock hills with trees"></div>
    <div class="photo ph-dusk" style="left:112px;top:80px;width:50px;height:20px" role="img" aria-label="Lake at sunset"></div>
    <div class="photo ph-valley" style="left:164px;top:80px;right:0;bottom:0" role="img" aria-label="Road towards mountains"></div>
    <div class="photo ph-lake" style="left:112px;top:102px;width:50px;bottom:0" role="img" aria-label="Lakeshore"></div>
  </section>

  <!-- 15 curve statement -->
  <section class="slide">
    <div class="photo ph-hills" style="inset:0" role="img" aria-label="Golden plains under a dramatic blue sky"></div>
    <svg class="abs" style="inset:0" width="218" height="122" viewBox="0 0 218 122" aria-hidden="true"><path d="M138 0 C150 55 175 95 218 118 V0 Z" fill="#fff"/></svg>
    <p class="abs statement right" style="right:8px;top:24px;width:64px;font-size:6px">Flexibility, Innovation And Future Focus/Vision Are What Our Clients Can Count On Us For.</p>
  </section>

  <!-- 16 work statement -->
  <section class="slide">
    <div class="photo ph-lake" style="left:0;top:0;right:0;height:62px" role="img" aria-label="Blue alpine lake with snowy range"></div>
    <p class="abs statement center" style="left:14px;right:14px;top:70px;font-size:7px">Work Is One Of Many Of Life's Great Facilitators, We Recognise And Value The Others - Its Not Just About Work.</p>
    <div class="footer"><div class="brand">Kauri Learning</div></div>
  </section>

  <!-- 17 profile -->
  <section class="slide">
    <p class="abs body" style="left:15px;top:18px;width:72px;font-size:2.8px;line-height:1.7;color:var(--green)">Lorem ipsum dolor sit amet, consectetur adipiscing elit. Nam leo nisi, molestie sit amet, lacinia sed, efficitur justo. Donec volutpat.</p>
    <div class="abs" style="left:15px;top:58px">
      <p class="skill">Marketing</p><div class="bar"><span style="width:80%"></span></div>
      <p class="skill">Communication</p><div class="bar"><span style="width:70%"></span></div>
      <p class="skill">Management</p><div class="bar"><span style="width:60%"></span></div>
    </div>
    <div class="photo ph-person" style="left:103px;top:0;width:55px;bottom:0" role="img" aria-label="Portrait of a smiling man in a dark suit"></div>
    <div class="green-v abs" style="left:158px;top:0;right:0;bottom:0"><p class="statement on-green abs" style="left:10px;bottom:12px;font-size:7.5px">Rowan<br>Tate</p></div>
  </section>

  <!-- 18 waterfall statement -->
  <section class="slide">
    <div class="photo ph-falls" style="left:0;top:0;width:54px;bottom:0" role="img" aria-label="Waterfall over a rock face"></div>
    <div class="photo ph-forest" style="left:56px;top:0;width:55px;bottom:0" role="img" aria-label="Green gorge from above"></div>
    <p class="abs statement" style="left:124px;top:22px;width:80px;font-size:7.2px">Flexibility, Innovation And Future Focus/Vision Are What Our Clients Can Count On Us For.</p>
  </section>

  <!-- 19 three photos + band -->
  <section class="slide">
    <div class="photo ph-valley" style="left:0;top:0;width:108px;height:80px" role="img" aria-label="Walking track through limestone hills"></div>
    <div class="photo ph-valley" style="left:110px;top:0;width:53px;height:80px" role="img" aria-label="Dry alpine hills"></div>
    <div class="photo ph-hills" style="left:165px;top:0;right:0;height:80px" role="img" aria-label="Trees on a ridge"></div>
    <div class="green abs" style="left:0;top:82px;right:0;bottom:0;padding:9px 20px"><p class="statement on-green center" style="font-size:5px">Work Is One Of Many Of Life's Great Facilitators, We Recognise And Value The Others - Its Not Just About Work.</p></div>
  </section>

  <!-- 20 curved photo with icon -->
  <section class="slide">
    <div class="photo ph-frost" style="left:126px;top:-30px;width:170px;height:180px;border-radius:50%" role="img" aria-label="Close-up of frosted leaves"></div>
    <svg class="abs" style="left:18px;top:40px" width="9" height="7" viewBox="0 0 18 14" fill="none" stroke="#3aad45" stroke-width="1.4"><path d="M1 5 6 1l3 3 3-3 5 4-8 8z"/></svg>
    <p class="abs" style="left:18px;top:50px;font-size:4px;color:var(--green)">Secret Bargains for Members</p>
    <p class="abs body" style="left:18px;top:57px;width:76px;line-height:1.8">Lorem ipsum dolor sit amet, consectetur adipiscing elit. Nam leo nisi, molestie sit amet, lacinia sed, efficitur justo. Donec volutpat.</p>
  </section>

  <!-- 21 curved photo with chat icon -->
  <section class="slide">
    <div class="photo ph-storm" style="left:132px;top:-20px;width:150px;height:150px;border-radius:50%" role="img" aria-label="Dark mountain reflected in water with a bird overhead"></div>
    <svg class="abs" style="left:28px;top:46px" width="8" height="7" viewBox="0 0 16 14"><path d="M8 1C4 1 1 3.4 1 6.3c0 1.5.8 2.8 2 3.8L2.5 13l3.5-2c.6.1 1.3.2 2 .2 4 0 7-2.4 7-5S12 1 8 1z" fill="#3aad45"/></svg>
    <p class="abs" style="left:28px;top:55px;font-size:4px;color:var(--green)">Secret Bargains for Members</p>
    <p class="abs body" style="left:28px;top:62px;width:76px;line-height:1.8">Lorem ipsum dolor sit amet, consectetur adipiscing elit. Nam leo nisi, molestie sit amet, lacinia sed, efficitur justo. Donec volutpat.</p>
  </section>

  <!-- 22 columns with centre panel -->
  <section class="slide">
    <div class="photo ph-lake" style="left:0;top:0;width:72px;height:60px" role="img" aria-label="Lake with rocky peaks"></div>
    <div class="photo ph-dusk" style="left:0;top:62px;width:72px;bottom:0" role="img" aria-label="Sunlit rocky hilltop"></div>
    <div class="green-v abs" style="left:74px;top:0;width:70px;bottom:0;padding:42px 6px 0"><p class="statement on-green" style="font-size:7px">We Think Life Is About People And Relationships</p></div>
    <div class="photo ph-lake" style="left:146px;top:0;right:0;height:60px" role="img" aria-label="Lake island with trees"></div>
    <div class="photo ph-dusk" style="left:146px;top:62px;right:0;bottom:0" role="img" aria-label="Hazy hills at sunset"></div>
  </section>

  <!-- 23 grid with band -->
  <section class="slide">
    <div class="photo ph-valley" style="left:0;top:0;width:71px;height:38px" role="img" aria-label="Rocky alpine plateau"></div>
    <div class="photo ph-lake" style="left:73px;top:0;width:72px;height:38px" role="img" aria-label="Fiord between steep cliffs"></div>
    <div class="photo ph-coast" style="left:147px;top:0;right:0;height:38px" role="img" aria-label="Lighthouse on a headland"></div>
    <div class="photo ph-forest" style="left:0;top:40px;width:71px;height:40px" role="img" aria-label="Green hillside"></div>
    <div class="green abs" style="left:71px;top:40px;right:0;height:40px;padding:7px 8px"><p class="statement on-green" style="font-size:5.6px">Work Is One Of Many Of Life's Great Facilitators, We Recognise And Value The Others - Its Not Just About Work.</p></div>
    <div class="photo ph-coast" style="left:0;top:82px;width:71px;bottom:0" role="img" aria-label="Sandy beach and surf"></div>
    <div class="photo ph-snow" style="left:73px;top:82px;width:72px;bottom:0" role="img" aria-label="Snowy mountain valley"></div>
    <div class="photo ph-lake" style="left:147px;top:82px;right:0;bottom:0" role="img" aria-label="Lake viewed from a hill"></div>
  </section>

  <!-- 24 header band with photos -->
  <section class="slide">
    <div class="green abs" style="left:0;top:0;right:0;height:33px;padding:5px 20px"><p class="statement on-green center" style="font-size:6.5px">Flexibility, Innovation And Future Focus/Vision</p></div>
    <div class="photo ph-sunset" style="left:0;top:35px;width:71px;bottom:0" role="img" aria-label="Wildflowers below a volcano at dusk"></div>
    <div class="photo ph-sunset" style="left:73px;top:35px;width:72px;bottom:0" role="img" aria-label="Volcano peak at dusk"></div>
    <div class="photo ph-sunset" style="left:147px;top:35px;right:0;bottom:0" role="img" aria-label="Alpine meadow at sunset"></div>
  </section>

  <!-- 25 thank you -->
  <section class="slide closing green-cover">
    <div class="photo" style="inset:0;background:linear-gradient(180deg,rgba(255,255,255,.08),rgba(0,0,0,.06))" role="img" aria-label="Green-toned mountain landscape"></div>
    <div class="brand large on-green abs" style="left:52px;top:92px">Kauri Learning</div>
    <div class="cover-line" style="left:52px;right:12px;top:106px"></div>
    <p class="abs" style="right:12px;top:94px;font-size:9px;color:#fff;font-weight:400">THANK YOU…</p>
  </section>

</main>
</body>
</html>
```